Corporate Business Card

Very professional, Modern, Not to busy, include phone address email, website
(555) 317-4860, 18716 52nd Avenue S, Harlan Bay, WA 98417, marcus@bralvintrust.example, vendrikworks.example

Target Market(s)

Manufacturing

Industry/Entity Type

Aero, machining, manufacturing, Off road racing

Contact Information for Business Card

Phone, address email, website

```html
<!DOCTYPE html>
<html lang="en">
<head>
<meta charset="utf-8">
<title>Vendrik Industries – Business Card</title>
<link href="https://fonts.googleapis.com/css2?family=Arimo:wght@400;700&display=swap" rel="stylesheet">
<style>
  :root {
    --backdrop: #d9d9db;
    --card-white: #f7f7f7;
    --navy: #15336b;
    --navy-tone: #2a4f8c;
    --navy-deep: #0f2858;
    --red: #d0212b;
    --ink: #3b3b3b;
    --muted: #7a7a7a;
    --divider: #cfcfcf;
  }
  * { box-sizing: border-box; margin: 0; padding: 0; }
  html, body {
    width: 1200px; height: 800px; overflow: hidden;
    background: var(--backdrop);
    font-family: "Arimo", Arial, sans-serif;
  }
  .canvas {
    width: 1200px; height: 800px;
    display: flex; align-items: center; justify-content: center; gap: 40px;
  }
  .card {
    width: 520px; height: 297px;
    border-radius: 22px;
    border-bottom: 3px solid var(--red);
    position: relative; overflow: hidden;
  }
  .card-front { background: var(--card-white); }
  .card-back { background: var(--navy); }

  .brand {
    display: flex; flex-direction: column; align-items: flex-start;
  }
  .brand-name {
    font-weight: 700; color: var(--navy);
    font-size: 40px; letter-spacing: 1px; line-height: 1;
  }
  .brand-sub {
    font-weight: 700; color: var(--navy);
    font-size: 15px; letter-spacing: 1px; margin-top: 6px; align-self: flex-end;
  }
  .brand-rule {
    height: 1px; width: 70%; background: var(--navy); margin-top: 10px;
  }

  .front-brand {
    position: absolute; left: 0; top: 0; width: 258px; height: 100%;
    display: flex; align-items: center; justify-content: center;
  }
  .front-divider {
    position: absolute; left: 258px; top: 0; width: 1px; height: 100%;
    background: linear-gradient(to bottom, transparent, var(--divider) 20%, var(--divider) 80%, transparent);
  }
  .front-details {
    position: absolute; left: 282px; top: 58px; right: 20px;
    color: var(--ink); font-size: 13px; line-height: 1.35;
  }
  .person-name { font-weight: 700; color: var(--navy); font-size: 19px; letter-spacing: 0.3px; }
  .person-title { color: var(--muted); font-size: 12px; margin-bottom: 14px; }
  .address { margin-bottom: 14px; }
  .contact-list { list-style: none; }
  .contact-list li { display: flex; align-items: center; gap: 8px; }
  .contact-list svg { width: 11px; height: 11px; fill: var(--red); flex: none; }

  .back-brand {
    position: absolute; inset: 0;
    display: flex; align-items: center; justify-content: center;
  }
  .back-brand .brand-name { color: var(--navy-tone); font-size: 68px; }
  .back-brand .brand-sub { color: var(--navy-tone); font-size: 24px; margin-top: 8px; }
  .back-brand .brand-rule { background: var(--navy-deep); margin-top: 14px; }
</style>
</head>
<body>
<main class="canvas">
  <section class="card card-front">
    <div class="front-brand">
      <div class="brand">
        <div class="brand-name">VENDRIK</div>
        <div class="brand-sub">Industries</div>
        <div class="brand-rule"></div>
      </div>
    </div>
    <div class="front-divider"></div>
    <div class="front-details">
      <div class="person-name">MARCUS HALDEN</div>
      <div class="person-title">Managing Director</div>
      <div class="address">18716 52nd Avenue S<br>Harlan Bay, WA 98417</div>
      <ul class="contact-list">
        <li><svg viewBox="0 0 24 24"><path d="M6.6 10.8a15.1 15.1 0 0 0 6.6 6.6l2.2-2.2a1 1 0 0 1 1-.25 11.4 11.4 0 0 0 3.6.57 1 1 0 0 1 1 1V20a1 1 0 0 1-1 1A17 17 0 0 1 3 4a1 1 0 0 1 1-1h3.5a1 1 0 0 1 1 1c0 1.25.2 2.45.57 3.57a1 1 0 0 1-.25 1z"/></svg>(555) 317-4860</li>
        <li><svg viewBox="0 0 24 24"><path d="M2 5h20v14H2zm2 2v.5l8 5 8-5V7l-8 5z"/></svg>marcus@bralvintrust.example</li>
        <li><svg viewBox="0 0 24 24"><circle cx="12" cy="12" r="10"/></svg>vendrikworks.example</li>
      </ul>
    </div>
  </section>

  <section class="card card-back">
    <div class="back-brand">
      <div class="brand">
        <div class="brand-name">VENDRIK</div>
        <div class="brand-sub">Industries</div>
        <div class="brand-rule"></div>
      </div>
    </div>
  </section>
</main>
</body>
</html>
```